Web Design with a Twist! Not cheap design

Please note that this project is ending at 5pm on Tuesday the 28th of September, Australian Western Standard Time!!

Please also note that this project has now been guaranteed!

This project involves three primary elements:
* Logo design;
* Web design - of additional pages and page elements to fit into a site that is already in design/development;
* Graphic design - various images used on the site.

The following materials are included for the project:
* Project requirements
* Company / Site name
* Company / Site description
* Wireframes for new pages / page elements
* Screenshots of existing designs and accompanying definition of constraints for new designs
* PSDs for existing site designs
* Technical requirements for designs
* Content (to guide designs)

Project Requirements:

* Logo design:
This is a new company / site, so we need a new logo. We want to see what you come up with here without giving too much direction that may restrict creativity. If desired, you may find possible guidance through considering the company name, company description, and the existing site designs. Please note that the current logo in the site is for placeholder purposes only.

* Web design:
We need the following pages (and features) to be designed for the site:
• Home page
• Advertise page
• How it works page
We’ve provided some wireframes for the pages, however we definitely don't want you to be guided by the layout/styling at all - the wireframes are only there to indicate the features that we require on each page only. So please ignore all aspects of the wireframes except for the indications of features and functionality.

* Graphic design:
We need various images to be designed throughout the site. These include:
• The image at the top of the ‘Home’ page – please note we will provide some direction on this asap
• The image at the top of the ‘Advertise’ page – please note we will provide some direction n this asap
• The image at the top of the ‘How it Works’ pages
• The images that accompany each of the left hand menu items on the ‘How it Works’ pages (the main images & thumbnails if that’s part of your design). Please note that these images need to be constructed to match the Headlines for each of the ‘What’, ‘Who’, ‘Where’, etc menu items. These Headlines (and some descriptive text) can be found in the Content section at the end of this brief.
• The map of Australia for the ‘Home’ page
• The images to accompany the pricing section of the ‘Advertise’ page
• The variations of the ‘Life in the search lane’ images that are used on the ‘Home’, ‘Advertise’, and ‘How it Works’ pages. Please note that if you want to use different imagery (or no imagery, dependent upon your design) for the Home and Advertise pages then this is your call.

Company Name:
TaskBloom

Company / Site description:
This site will provide a means for contractors ('advertisers') to easily specify and advertise their services, coupled with a means for employers (‘buyers’) to easily seek out and contact these people.
The site will cater for contractor-side advertisements only; job postings will not be accommodated (turning the traditional job advertisement model on its head).
In general, the functionality of the site is somewhat like a mashup of sites like crewvault.com and stayvane.com. The site will incorporate the following primary features of contractor profile display and search, company profile display, (and an availability calendar for v2 release).

Constraints for designs:
On some of the existing designs you will notice that a number of the elements of the site have already been designed. When constructing your designs, please work in accordance with the following constraints:

You have to keep:
• Colour scheme in the header
• Colour scheme in the top navigation buttons (including text colour and background colour)
• Colour scheme for the buttons like on the Register page

You can ignore:
• The existing placeholder logo
• Border, layout, and colour scheme for page elements (like the lines around and inside the register section on the Register page)
• Design of text fields
• Font colour scheme throughout the site – the orange and grey headlines and body text
• Design and colour scheme of the map of Australia
• The breadcrumbs (whether or not they appear, and their layout, styling, colour scheme etc)
• Dropdown styling (assuming you had to make some; currently not on any pages we’re asking you to do) like on the Browse Profession page
• Profile styling (for the home page featured profiles) like on the Browse Profession page
• Footer styling
• Anything else we haven’t explicitly asked you to keep

Technical requirements for design:
Any site designs in either Layered Pixelry files (PSD's) or Illustrator Drawings (AI). RGB Color. Must fit current site design, we work to 1024 wide screens. Usuable area is defined in site designs that are attached in the Pixelry documents; it's around 960px.
Logo work needs to be Illustrator Drawings (AI) and EPS. Need CMYK images for printing and RGB for screen. Logos must include any special fonts that are used as TTF or Open Type. Logos need Color, Monochrome, Reversed and both Tall and Wide usages.

Content for the 'How it Works' pages - this content should guide the images that appear on each page.
* What
Headline: TaskBloom brings contractors and employers together
Descriptive text: (turns the traditional job search model on its head)
* Who
Headline: TaskBloom is for highly skilled professionals and fast moving companies
Descriptive text:
* Where
Headline: Anywhere in Australia, TaskBloom is working by your side
Descriptive text:
* Why
Headline: There are more than 1 million reasons to love TaskBloom
Descriptive text: In Australia, there are 1 million people who work as contractors in their main job, and a further 100,000 people who are contractors in their second job. That’s a lot of contractors!
* When
Headline: TaskBloom is forming partnerships 24 hours a day
Descriptive text:
* How
Headline: Life in the search lane, with TaskBloom
Descriptive text: Advertise on TaskBloom now, and get your life in the search lane.

Remember
Just remember the wireframes we have submitted are just a guide – we want to see your creativity shine. And above all else - have fun!
Thank you.
Updates

Please note the deadline for this design competition 5pm on Tuesday the 28th of September, Australian Western Standard Time.

Just under 3 days away!

The deadline of the project will soon be updated to reflect this.

Hi Designers!

Just to be 100% clear about the deadline - the timer is currently showing 7 hours too many. In other words, the project will end 7 hours before the timer finishes.

I will send a notification if the timer starts to display the correct time. So until then, please remember that the deadline is earlier than it seems!

Thanks

Hi Designers,

A couple of really important points:

Firstly - if everyone could please stick to the theme that we provided in the Pixelry files that would be excellent. It is not possible for us to create a new theme. We're dealing with very tight deadlines, so please just provide designs that fit within the current theme.

Secondly, we were really hoping for more illustrations / graphics to be provided in the designs. We're not a fan of the stock photos of generic business people. So please send through designs that incorporate illustrations / graphics for any imagery.

Also just a reminder that this competition is still ending 7 hours earlier than the timer currently displays.

Thanks.

Target Market(s)

The ‘advertiser’ target market for the site is white collar professionals, in all types of industries. The site will be catering for premium contractors only. The site will be catering for both 'in person' contractors, as well as 'knowledge economy' contractors. The site will not be seeking to compete with gigmora.com, plixo.com, taskrune.com, or similar sites.

The advertiser target market will also encompass companies and labour hire agencies that have contractors in their workforce.

The ‘buyer’ target market will encompass employers, recruitment agents, and member-to-member hiring.

Industry/Entity Type

Contractor

Requirements
Must have
• As per overview
Nice to have
• As per overview
Should not have
• As per overview

```html
<!DOCTYPE html>
<html lang="en">
<head>
<meta charset="utf-8">
<title>TaskBloom – Home</title>
<link href="https://fonts.googleapis.com/css2?family=Arimo:wght@400;700&family=Noto+Sans:ital,wght@0,400;0,700;1,400&family=Roboto+Condensed:wght@400;700&display=swap" rel="stylesheet">
<style>
:root{
  --page:#f1f1f1;
  --header:#64768e;
  --header-dark:#56677f;
  --tab:#bcc3cc;
  --tab-text:#9aa2ad;
  --tab-active-text:#8a8a8a;
  --white:#ffffff;
  --orange:#ff6a13;
  --orange-soft:#ff8533;
  --ink:#444a52;
  --slate:#5a6a80;
  --muted:#a6acb4;
  --card:#efefef;
  --footer-ink:#5b6475;
}
*{margin:0;padding:0;box-sizing:border-box}
html,body{width:1200px;height:1154px;overflow:hidden}
body{background:var(--page);position:relative;font-family:"Noto Sans",Verdana,sans-serif;color:var(--ink)}
.abs{position:absolute}
.header-band{left:0;top:0;width:1200px;height:97px;background:linear-gradient(180deg,var(--header-dark),var(--header))}
.tab{top:65px;height:32px;background:var(--tab);border-radius:9px 9px 0 0;font:700 22px/34px "Arimo",Arial,sans-serif;color:var(--tab-text);text-align:center}
.tab.active{background:var(--white);color:var(--tab-active-text)}
.hero{left:117px;top:111px;width:969px;height:267px;background:radial-gradient(ellipse at 30% 40%,#6fb83e 0%,#3f8a22 45%,#2e6a1a 100%)}
.brand{left:147px;top:150px;z-index:3;display:flex;align-items:center;gap:10px}
.brand-mark{width:22px;height:22px;background:var(--orange)}
.brand-name{font:700 34px/1 "Arimo",Arial,sans-serif;color:var(--white)}
.hero-tagline{left:490px;top:143px;font:400 22px/1.05 "Roboto Condensed",sans-serif;color:var(--white)}
.hero-tagline b{font-size:29px;font-weight:400;display:block}
.hero-photo{border:3px solid var(--white);border-radius:0 0 18px 0}
.photo-call{left:485px;top:216px;width:279px;height:138px;background:linear-gradient(135deg,#c9ccd0,#8a7a70 60%,#5a3b34)}
.photo-swatch{left:810px;top:147px;width:236px;height:205px;border-radius:14px 0 14px 0;background:linear-gradient(200deg,#7a2a2a,#d05a3a 35%,#e0b030 65%,#c8c090)}
.main{left:117px;top:401px;width:969px;height:653px;background:var(--white)}
.section-title{font-size:19px;color:var(--orange);font-weight:400}
.map{left:160px;top:458px;width:295px;height:254px;background:linear-gradient(160deg,#b4c2d3,#8d9aae);border-radius:40% 45% 40% 30%}
.label{font-size:13px;color:#666;letter-spacing:.3px}
.state-list{left:495px;top:461px;list-style:none}
.state-list li{font:700 13px/20px "Noto Sans",Verdana,sans-serif;color:var(--orange);letter-spacing:1px}
.search-field{left:495px;top:666px;width:235px;height:19px;border:1px solid #aaa;background:var(--white)}
.btn{height:24px;border-radius:3px;background:linear-gradient(180deg,#ff9a3c,#ff6a13 60%,#d84a00);color:var(--white);font:700 13px/24px "Noto Sans",sans-serif;text-align:center;letter-spacing:.5px}
.welcome-title{left:148px;top:780px;font-size:16px;color:var(--slate)}
.copy{font-size:11px;line-height:14px;letter-spacing:1px;color:var(--ink)}
.cta{left:477px;top:900px;width:275px;height:134px;background:var(--orange-soft);border-radius:22px 0 22px 0;color:var(--white);padding:14px 0 0 23px;letter-spacing:1.5px;font-weight:700}
.cta .big{font-size:29px;line-height:34px}
.cta .mid{font-size:18px;line-height:20px}
.cta .find{font-size:24px;line-height:30px;margin-top:10px}
.profile{left:812px;width:232px;height:161px;background:var(--card);padding:13px 0 0 17px}
.avatar{width:68px;height:68px;background:linear-gradient(180deg,#9a9088,#4e4843);border:1px solid #888;position:absolute;left:17px;top:13px}
.profile-head{margin-left:84px;height:80px}
.profile-name{font:700 12.5px/18px "Arimo",Arial,sans-serif;color:var(--orange);letter-spacing:-.3px}
.profile-role{font:700 12px/20px "Arimo",Arial,sans-serif;color:#7d838c;letter-spacing:-.3px}
.profile-role.tight{line-height:14px;margin-top:3px}
.profile-skills{font:400 12px/14px "Arimo",Arial,sans-serif;color:var(--muted);letter-spacing:-.3px}
.profile-skills em{display:block}
.footer-col{top:1066px}
.footer-col h3{font:700 18px/22px "Roboto Condensed",sans-serif;color:var(--footer-ink)}
.footer-col a{display:block;font:400 16px/18px "Roboto Condensed",sans-serif;color:var(--footer-ink);text-decoration:none}
</style>
</head>
<body>
<div class="abs header-band"></div>
<nav>
  <div class="abs tab active" style="left:337px;width:114px">Home</div>
  <div class="abs tab" style="left:461px;width:114px">Find</div>
  <div class="abs tab" style="left:585px;width:131px">Advertise</div>
  <div class="abs tab" style="left:727px;width:153px">How it Works</div>
  <div class="abs tab" style="left:888px;width:95px">Blog</div>
  <div class="abs tab" style="left:993px;width:92px">Login</div>
</nav>

<div class="abs hero" role="img" aria-label="Close-up of green grass blades, softly blurred"></div>
<div class="abs brand"><span class="brand-mark"></span><span class="brand-name">TaskBloom</span></div>
<div class="abs hero-tagline">find highly skilled<b>professionals</b></div>
<div class="abs hero-photo photo-call" role="img" aria-label="Businesswoman on the phone reading a newspaper"></div>
<div class="abs hero-photo photo-swatch" role="img" aria-label="Fanned paint colour swatch cards"></div>

<main class="abs main"></main>
<h2 class="abs section-title" style="left:146px;top:413px">Browse Contractors</h2>
<div class="abs map" role="img" aria-label="Map of Australia divided by state and territory"></div>
<div class="abs label" style="left:494px;top:432px">By State</div>
<ul class="abs state-list">
  <li>Western Australia</li><li>South Australia</li><li>Nortnern Territory</li><li>Queensland</li>
  <li>New South Wales</li><li>Victoria</li><li>Australian Capital Territory</li><li>Tasmania</li>
</ul>
<div class="abs label" style="left:495px;top:641px">Keyword search</div>
<div class="abs search-field"></div>
<div class="abs btn" style="left:495px;top:692px;width:235px">Find contractors</div>

<h2 class="abs welcome-title" style="font-weight:400">Welcome to TaskBloom!</h2>
<p class="abs copy" style="left:149px;top:816px;width:590px">Donec gravida, sapien a fringilla posuere, augue ante lobortis ipsum, sit amet tincidunt ante leo a eros. Vivamus non odio nisi. Nulla cursus, metus in porttitor aliquam, leo nunc dignissim mi, id.</p>
<p class="abs copy" style="left:149px;top:858px;width:590px">Vestibulum mauris odio, vulputate vitae ornare non, sollicitudin eget nisi. Quisque varius, nibh vitae consectetur.</p>
<p class="abs copy" style="left:149px;top:900px;width:310px">Lorem ipsum dolor sit amet, consectetur adipiscing elit. Praesent commodo fermentum ultrices. Quisque molestie metus sed lacus aliquam quis congue enim blandit. Donec sollicitudin, nibh ut porttitor dapibus, nulla erat scelerisque nisl, ut ornare tortor sapien at mauris. Sed ac tortor mi, vitae tempor justo. Vestibulum ut nunc elit. Nulla vitae interdum urna. Vivamus bibendum accumsan orci eget interdum.</p>
<div class="abs cta">
  <div class="big">How it works!</div>
  <div class="mid">Life in the search lane</div>
  <div class="find">FIND OUT HERE!</div>
</div>

<h2 class="abs section-title" style="left:816px;top:413px">Features Profiles</h2>
<article class="abs profile" style="top:451px">
  <div class="avatar" role="img" aria-label="Profile photo"></div>
  <div class="profile-head"><div class="profile-name">Lukas Brennard</div><div class="profile-role">Designer, Developer,<br>Producer</div></div>
  <div class="profile-skills">QueryKit, Pixelry, WebForge,<br>Project Management, Editorial,<br>Photography, Consultancy<em>Servicing all states</em></div>
</article>
<article class="abs profile" style="top:633px">
  <div class="avatar" role="img" aria-label="Profile photo"></div>
  <div class="profile-head"><div class="profile-name">Lukas Brennard</div><div class="profile-role">Designer, Developer,<br>Producer</div></div>
  <div class="profile-skills">QueryKit, Pixelry, WebForge,<br>Project Management, Editorial,<br>Photography, Consultancy<em>Servicing all states</em></div>
</article>
<article class="abs profile" style="top:815px">
  <div class="avatar" role="img" aria-label="Profile photo"></div>
  <div class="profile-head"><div class="profile-name">Owen Castell</div><div class="profile-role tight">Consultant, Developer,<br>All-round nice guy</div></div>
  <div class="profile-skills">C#, Domain Modeling, Stackline MVC,<br>Active Record, SQL<em>Servicing New South Wales, Victoria<br>and New South Wales</em></div>
</article>
<div class="abs btn" style="left:809px;top:992px;width:235px">Find contractors</div>

<footer>
  <div class="abs footer-col" style="left:146px"><h3>The service</h3><a href="#">About</a><a href="#">Browse</a><a href="#">Log in</a></div>
  <div class="abs footer-col" style="left:476px"><h3>Support</h3><a href="#">Contact us</a><a href="#">FAQ</a></div>
  <div class="abs footer-col" style="left:788px"><h3>Legal</h3><a href="#">Privacy Policy</a><a href="#">terms &amp; Conditions</a></div>
</footer>
</body>
</html>
```